Under Still Skies Stationary Design Pkg
Business Card, Letterhead, #10 Envelope, 4 X 6 Notecard
Under Still Skies Stationary Design Pkg -
Creative Brief
Simple
Marla Quint
Coach/Writer/Speaker
2847 W. Fallow Lane Suite 310 Phoenix, Arizona 85093
marla@understillskies.example
www.understillskies.example
Contest is for a business card, standard letterhead, #10 envelope, and a 4 1/4 X 6 1/4 note card design. Please use the light and dark gray colors from the design. No big solids. On the note card design, please only use the my name (Marla Quint) and logo w/o company name or tag lines. Thank you. I look forward to seeing what you come up with.

```html
<!DOCTYPE html>
<html lang="en">
<head>
<meta charset="utf-8">
<title>Under Still Skies Stationery Package</title>
<link rel="stylesheet" href="https://fonts.googleapis.com/css2?family=Cormorant+Garamond:wght@500&family=Lato:wght@400;700&display=swap">
<style>
  :root {
    --stage: #000000;
    --paper: #ffffff;
    --paper-shade: #f1f1f1;
    --gray-light: #c9c9c9;
    --gray-mid: #9a9a9a;
    --gray-dark: #6d6d6d;
    --ink: #5a5a5a;
    --shadow: rgba(0,0,0,0.45);
  }
  * { box-sizing: border-box; margin: 0; padding: 0; }
  html, body { width: 1200px; height: 598px; overflow: hidden; background: var(--stage); }
  .canvas { position: relative; width: 1200px; height: 598px; overflow: hidden; background: var(--stage); font-family: "Lato", sans-serif; color: var(--ink); }

  .piece { position: absolute; overflow: hidden; box-shadow: 0 2px 8px var(--shadow); }
  .paper-white { background: linear-gradient(135deg, var(--paper) 0%, var(--paper-shade) 100%); }
  .paper-gray { background: linear-gradient(135deg, var(--gray-mid) 0%, #a8a8a8 100%); }

  .brand { display: flex; align-items: center; gap: 6px; }
  .brand-dot { border-radius: 50%; background: var(--gray-mid); flex: none; }
  .brand-name { font-family: "Cormorant Garamond", serif; font-weight: 500; color: var(--gray-dark); letter-spacing: 0.05em; text-transform: uppercase; white-space: nowrap; }
  .tagline { font-size: 5px; color: var(--gray-mid); letter-spacing: 0.1em; text-transform: uppercase; white-space: nowrap; }

  /* Note cards */
  .notecard { left: 103px; width: 317px; }
  .notecard--white { top: 89px; height: 216px; }
  .notecard--gray { top: 319px; height: 202px; }
  .notecard-sign { position: absolute; right: 8px; display: flex; align-items: center; gap: 8px; }
  .notecard--white .notecard-sign { bottom: 30px; }
  .notecard--gray .notecard-sign { bottom: 16px; }
  .notecard-sign .brand-dot { width: 18px; height: 18px; }
  .notecard-name { font-weight: 700; font-size: 14px; white-space: nowrap; }
  .notecard--white .notecard-name { color: var(--gray-dark); }
  .notecard--gray .notecard-name { color: var(--paper); }
  .notecard--gray .brand-dot { background: var(--paper); }

  /* Letterhead */
  .letterhead-back { left: 474px; top: 106px; width: 341px; height: 440px; background: var(--gray-mid); transform: rotate(-3deg); }
  .letterhead { left: 437px; top: 89px; width: 341px; height: 439px; }
  .letterhead-head { position: absolute; left: 20px; top: 12px; display: flex; flex-direction: column; align-items: flex-start; gap: 2px; }
  .letterhead-head .brand-dot { width: 14px; height: 14px; }
  .letterhead-head .brand-name { font-size: 18px; }
  .letterhead-head .tagline { padding-left: 20px; }
  .letterhead-foot { position: absolute; left: 14px; right: 14px; bottom: 10px; display: flex; justify-content: space-between; font-size: 4.6px; color: var(--gray-mid); white-space: nowrap; }

  /* Envelopes */
  .envelope-flap { position: absolute; inset: 0; width: 100%; height: 100%; }
  .envelope--back { left: 704px; top: 109px; width: 310px; height: 130px; transform: rotate(10deg); }
  .envelope--gray { left: 880px; top: 205px; width: 175px; height: 145px; background: var(--gray-light); transform: rotate(6deg); }
  .envelope--front { left: 701px; top: 221px; width: 319px; height: 134px; }
  .envelope-return { position: absolute; left: 14px; top: 10px; }
  .envelope-return .brand-dot { width: 10px; height: 10px; }
  .envelope-return .brand-name { font-size: 12px; }
  .envelope-address { position: absolute; left: 14px; bottom: 8px; font-size: 5px; color: var(--gray-mid); white-space: nowrap; }

  /* Business cards */
  .bizcard { height: 60px; }
  .bizcard--top-back { left: 864px; top: 367px; width: 122px; }
  .bizcard--top-front { left: 882px; top: 370px; width: 122px; }
  .bizcard--bl-back { left: 799px; top: 456px; width: 116px; }
  .bizcard--bl-front { left: 816px; top: 458px; width: 116px; }
  .bizcard--br-front { left: 955px; top: 458px; width: 106px; }
  .bizcard-content { position: absolute; inset: 0; display: flex; flex-direction: column; justify-content: center; padding: 0 8px; gap: 3px; }
  .bizcard .brand { gap: 4px; }
  .bizcard .brand-dot { width: 7px; height: 7px; }
  .bizcard .brand-name { font-size: 7px; letter-spacing: 0.03em; }
  .bizcard-detail { font-size: 4.6px; color: var(--gray-mid); white-space: nowrap; }
  .bizcard-detail--right { align-self: flex-end; font-weight: 700; font-size: 5px; color: var(--gray-dark); }
</style>
</head>
<body>
<main class="canvas">

  <section class="piece notecard notecard--white paper-white" aria-label="Note card, white">
    <div class="notecard-sign"><span class="brand-dot"></span><span class="notecard-name">Marla Quint</span></div>
  </section>

  <section class="piece notecard notecard--gray paper-gray" aria-label="Note card, gray">
    <div class="notecard-sign"><span class="brand-dot"></span><span class="notecard-name">Marla Quint</span></div>
  </section>

  <div class="piece letterhead-back" aria-hidden="true"></div>
  <section class="piece letterhead paper-white" aria-label="Letterhead">
    <header class="letterhead-head">
      <div class="brand"><span class="brand-dot"></span><span class="brand-name">Under Still Skies</span></div>
      <span class="tagline">Coach · Writer · Speaker</span>
    </header>
    <footer class="letterhead-foot">
      <span>2847 W. Fallow Lane Suite 310 Phoenix, Arizona 85093</span>
      <span>602.555.0182</span>
      <span>marla@understillskies.example</span>
      <span>www.understillskies.example</span>
    </footer>
  </section>

  <div class="piece envelope--back paper-white" aria-hidden="true">
    <svg class="envelope-flap" viewBox="0 0 310 130" preserveAspectRatio="none"><polyline points="0,0 155,62 310,0" fill="none" stroke="#bdbdbd" stroke-width="1.5"/></svg>
  </div>
  <div class="piece envelope--gray" aria-hidden="true"></div>
  <section class="piece envelope--front paper-white" aria-label="Number 10 envelope">
    <div class="envelope-return">
      <div class="brand"><span class="brand-dot"></span><span class="brand-name">Under Still Skies</span></div>
    </div>
    <p class="envelope-address">2847 W. Fallow Lane Suite 310 Phoenix, Arizona 85093</p>
  </section>

  <div class="piece bizcard bizcard--top-back paper-gray" aria-hidden="true"></div>
  <section class="piece bizcard bizcard--top-front paper-white" aria-label="Business card back">
    <div class="bizcard-content">
      <span class="bizcard-detail bizcard-detail--right">Marla Quint</span>
      <span class="bizcard-detail" style="align-self:flex-end">Coach/Writer/Speaker</span>
    </div>
  </section>

  <div class="piece bizcard bizcard--bl-back paper-gray" aria-hidden="true"></div>
  <section class="piece bizcard bizcard--bl-front paper-white" aria-label="Business card front">
    <div class="bizcard-content">
      <div class="brand"><span class="brand-dot"></span><span class="brand-name">Under Still Skies</span></div>
    </div>
  </section>

  <section class="piece bizcard bizcard--br-front paper-white" aria-label="Business card front, alternate">
    <div class="bizcard-content">
      <div class="brand"><span class="brand-dot"></span><span class="brand-name">Under Still Skies</span></div>
      <span class="bizcard-detail">www.understillskies.example</span>
    </div>
  </section>

</main>
</body>
</html>
```